Harbor Zentrik needs a new Website Design

We need a WEB site landing page (/template) design, we currently have a company logo.We like the Valtor.com web designEnclosed is our company logo.Our Current website is https://www.harborzentrik.com.au/

1 page

```html
<!DOCTYPE html>
<html lang="en">
<head>
<meta charset="utf-8">
<title>Zentrik UC — White-Label Communications</title>
<link href="https://fonts.googleapis.com/css2?family=Poppins:wght@300;400;500;600&display=swap" rel="stylesheet">
<style>
:root{
  --black:#000;
  --blue:#0b5ea8;
  --navy:#0d4a8a;
  --sky:#1a9be6;
  --text:#222;
  --muted:#555;
  --white:#fff;
  --field-border:#cfd6de;
}
*{box-sizing:border-box;margin:0;padding:0}
html,body{width:1200px;height:3073px;overflow:hidden}
body{font-family:'Poppins',sans-serif;color:var(--text);background:var(--white);position:relative}
a{color:inherit;text-decoration:none}

/* header */
.site-header{position:absolute;left:0;top:0;width:1200px;height:124px;background:var(--black);color:var(--white)}
.brand{position:absolute;display:flex;align-items:center;gap:10px;color:var(--sky);font-weight:400;white-space:nowrap}
.brand .dot{width:26px;height:26px;border-radius:50%;background:var(--sky)}
.site-header .brand{left:152px;top:42px;font-size:38px}
.top-contact{position:absolute;top:30px;right:142px;display:flex;gap:28px;font-size:15px;align-items:center}
.top-contact span{display:flex;align-items:center;gap:10px}
.main-nav{position:absolute;top:88px;right:142px;display:flex;gap:27px;font-size:16px}
.main-nav .active{color:var(--sky);font-weight:500}

/* hero */
.hero-media{position:absolute;left:0;top:124px;width:1200px;height:530px;background:linear-gradient(100deg,#3b6f96 0%,#5d8fb5 40%,#3b6e98 65%,#1d3a5c 100%)}
.hero-title{position:absolute;left:142px;top:281px;color:var(--white);font-size:39px;line-height:47px;font-weight:400}
.btn{position:absolute;background:var(--sky);color:var(--white);border-radius:16px;font-size:13px;display:flex;align-items:center;justify-content:center}
.slide-arrow{position:absolute;top:377px;width:32px;height:28px;background:#d8dde2;display:flex;align-items:center;justify-content:center}

/* components */
.section-title{position:absolute;left:0;width:1200px;text-align:center;font-size:25px;line-height:29px;font-weight:500}
.section-sub{position:absolute;left:0;width:1200px;text-align:center;font-size:13px;color:var(--muted)}
.rule{position:absolute;height:3px;background:var(--blue)}
.service{position:absolute;width:180px;text-align:center}
.service .ring{width:124px;height:124px;border-radius:50%;border:3px solid var(--navy);margin:0 auto;display:flex;align-items:center;justify-content:center;background:var(--white)}
.service.active .ring{background:var(--sky);border-color:var(--navy)}
.service .label{margin-top:46px;font-size:17px;line-height:24px;color:#333}
.service.active .label{color:var(--blue)}

.pbx-diagram{position:absolute;left:142px;top:1107px;width:446px;height:283px;background:#e4e6e8;box-shadow:0 10px 14px -8px rgba(0,0,0,.25)}
.feature{position:absolute;left:630px;top:1120px;width:440px}
.feature h2{font-size:25px;font-weight:400;line-height:34px}
.feature h3{font-size:17px;font-weight:500;margin-top:26px;line-height:24px}
.feature p{font-size:12.5px;line-height:23px;color:#444;margin-top:4px}

/* support band */
.support-band{position:absolute;left:0;top:1508px;width:1200px;height:379px;background:linear-gradient(90deg,#0d2d5e 0%,#2b72b8 25%,#163f7a 45%,#1b3c6f 60%,#8a4a3a 80%,#c2622e 100%)}
.support{position:absolute;left:607px;top:1630px;color:var(--white)}
.support h2{font-size:40px;font-weight:500;margin-left:140px}
.support h3{font-size:22px;font-weight:400;margin-top:12px}
.support p{font-size:17px;line-height:30px}

/* why */
.team-photo{position:absolute;left:143px;top:1965px;width:394px;height:245px;background:linear-gradient(135deg,#c9cfd6,#6d7682 60%,#e2e4e6)}
.logo-tile{position:absolute;left:330px;top:2160px;width:207px;height:135px;background:var(--black)}
.logo-tile .brand{left:22px;top:50px;font-size:26px}
.why{position:absolute;left:590px;top:1975px;width:470px}
.why h2{font-size:32px;color:var(--sky);font-weight:400;display:flex;align-items:center;gap:12px}
.why h2 .dot{width:34px;height:34px;border-radius:50%;background:var(--sky)}
.why p{font-size:13px;line-height:25px;color:#333;margin-top:28px}
.why ul{list-style:none;margin-top:10px}
.why li{font-size:13px;color:#333;display:flex;gap:14px;align-items:center;height:33px}

/* footer */
.footer-bg{position:absolute;left:0;top:2702px;width:1200px;height:371px;background:linear-gradient(180deg,#2a70b8 0%,#1b5aa3 50%,#0e3f80 100%)}
.inquiry{position:absolute;left:247px;top:2380px;width:706px;height:376px;background:var(--white);box-shadow:0 2px 8px rgba(0,0,0,.15);border-top:4px solid #5a9ad6;border-bottom:4px solid #5a9ad6}
.inquiry h2{position:absolute;top:28px;width:100%;text-align:center;font-size:27px;font-weight:400;color:#333}
.field{position:absolute;height:42px;border:1px solid var(--field-border);display:flex;align-items:flex-start;font-size:11px;color:#555}
.field .ico{width:36px;height:40px;border-right:1px solid var(--field-border);display:flex;align-items:center;justify-content:center}
.field .ph{padding:13px 12px}
.submit{position:absolute;left:296px;top:296px;width:113px;height:30px;border-radius:16px;background:var(--sky);color:var(--white);font-weight:500;font-size:16px;display:flex;align-items:center;justify-content:center}

.footer{color:var(--white);font-size:13px}
.footer h4{position:absolute;font-size:14px;font-weight:500;border-bottom:1px solid rgba(255,255,255,.5)}
.links{position:absolute;left:143px;top:2852px;list-style:none;line-height:24px}
.ccol{position:absolute;line-height:22px}
.ccol .row{display:flex;gap:10px;align-items:center}
.social{display:flex;gap:10px;margin-top:8px}
.social span{width:24px;height:24px;border-radius:50%;background:var(--white)}
.copyright{position:absolute;left:0;top:3033px;width:1200px;text-align:center;font-size:13px;color:var(--white)}
</style>
</head>
<body>

<header class="site-header">
  <div class="brand"><span class="dot"></span>Zentrik UC</div>
  <div class="top-contact">
    <span><svg width="20" height="20" viewBox="0 0 24 24"><path d="M6.6 10.8a15 15 0 006.6 6.6l2.2-2.2a1 1 0 011-.25 11 11 0 003.5.56 1 1 0 011 1V20a1 1 0 01-1 1A17 17 0 013 4a1 1 0 011-1h3.5a1 1 0 011 1c0 1.25.2 2.45.56 3.57a1 1 0 01-.25 1z" fill="none" stroke="#1a9be6" stroke-width="1.6"/></svg>612.555.01234</span>
    <span style="color:#444">|</span>
    <span><svg width="20" height="18" viewBox="0 0 24 20"><rect x="2" y="3" width="20" height="14" fill="none" stroke="#1a9be6" stroke-width="1.6"/><path d="M2 3l10 8 10-8" fill="none" stroke="#1a9be6" stroke-width="1.6"/></svg>support@harborzentrik.com.au</span>
  </div>
  <nav class="main-nav">
    <a class="active">Home</a><a>Voice</a><a>Data</a><a>Hardware</a><a>Services Request</a><a>Contact Us</a>
  </nav>
</header>

<div class="hero-media" role="img" aria-label="Hand touching a glowing ring of network and device icons"></div>
<h1 class="hero-title">White-Label Solution<br>For All Your<br>Communication Needs</h1>
<a class="btn" style="left:142px;top:440px;width:148px;height:32px">Contact Us Today</a>
<div class="slide-arrow" style="left:2px"><svg width="10" height="12"><path d="M7 1L2 6l5 5" stroke="#222" stroke-width="2" fill="none"/></svg></div>
<div class="slide-arrow" style="left:1166px"><svg width="10" height="12"><path d="M3 1l5 5-5 5" stroke="#222" stroke-width="2" fill="none"/></svg></div>

<h2 class="section-title" style="top:711px">We Have All The Components<br>To Start And Run Your Own White Label Telco</h2>
<p class="section-sub" style="top:771px">Liberating Businesses from Traditional Communications Systems</p>
<div class="rule" style="left:566px;top:804px;width:70px"></div>

<div class="service active" style="left:113px;top:833px">
  <div class="ring"><svg width="64" height="64" viewBox="0 0 64 64"><path d="M16 40a10 10 0 010-20 14 14 0 0127-4 10 10 0 015 19" fill="none" stroke="#fff" stroke-width="3"/><rect x="22" y="30" width="22" height="26" rx="3" fill="#fff"/><g fill="#1a9be6"><rect x="26" y="35" width="4" height="3"/><rect x="32" y="35" width="4" height="3"/><rect x="26" y="41" width="4" height="3"/><rect x="32" y="41" width="4" height="3"/><rect x="26" y="47" width="4" height="3"/><rect x="32" y="47" width="4" height="3"/></g></svg></div>
  <div class="label">Cloud IP<br>PBX</div>
</div>
<div class="service" style="left:313px;top:833px">
  <div class="ring"><svg width="64" height="64" viewBox="0 0 64 64"><path d="M14 38a10 10 0 010-20 14 14 0 0127-4 10 10 0 015 19" fill="none" stroke="#0d4a8a" stroke-width="2.5"/><rect x="10" y="30" width="24" height="16" rx="3" fill="#0d4a8a"/><rect x="28" y="36" width="26" height="18" rx="3" fill="#fff" stroke="#0d4a8a" stroke-width="2.5"/><path d="M33 42h16M33 47h12" stroke="#0d4a8a" stroke-width="2"/></svg></div>
  <div class="label">Unified<br>Communications</div>
</div>
<div class="service" style="left:541px;top:833px">
  <div class="ring"><svg width="64" height="64" viewBox="0 0 64 64"><rect x="18" y="10" width="28" height="26" fill="none" stroke="#0d4a8a" stroke-width="2.5"/><path d="M23 17h18M23 22h18" stroke="#0d4a8a" stroke-width="2"/><rect x="10" y="28" width="44" height="26" fill="none" stroke="#0d4a8a" stroke-width="2.5"/><path d="M10 28l22 16 22-16M10 54l16-14M54 54L38 40" fill="none" stroke="#0d4a8a" stroke-width="2.5"/></svg></div>
  <div class="label">Invoice &amp; Payment<br>Platform</div>
</div>
<div class="service" style="left:738px;top:833px">
  <div class="ring"><svg width="64" height="64" viewBox="0 0 64 64" fill="none" stroke="#0d4a8a" stroke-width="2.5"><rect x="24" y="8" width="16" height="12"/><rect x="14" y="26" width="36" height="8"/><path d="M32 20v6M18 34v8M32 34v8M46 34v8"/><rect x="10" y="42" width="14" height="12"/><rect x="25" y="42" width="14" height="12"/><rect x="40" y="42" width="14" height="12"/></svg></div>
  <div class="label">Data<br>Services</div>
</div>
<div class="service" style="left:906px;top:833px">
  <div class="ring"><svg width="64" height="64" viewBox="0 0 64 64" fill="none" stroke="#0d4a8a" stroke-width="2.5"><circle cx="38" cy="24" r="12"/><path d="M38 14v8"/><path d="M16 20c-4 4-4 12 4 22s18 14 22 10l3-4-7-6-4 3c-3-1-9-7-10-10l3-4-6-7z"/></svg></div>
  <div class="label">Voice<br>Services</div>
</div>

<div class="pbx-diagram" role="img" aria-label="Diagram of a hosted PBX cloud linking headquarters, branch, regional and home offices"></div>
<div class="feature">
  <h2>Cloud IP PBX</h2>
  <div class="rule" style="left:0;top:46px;width:120px;height:2px"></div>
  <h3>Multiple IP PBXs on a single instance</h3>
  <p>A Multi-Tenant CloudPBX is able to handle multiple customers (tenants) with a single instance of the software. Even though every customer has a dedicated PBX, they all share the same Voxcore instance. Using the single instance for all customers cuts down operating costs significantly.</p>
</div>
<a class="btn" style="left:631px;top:1339px;width:148px;height:31px">Contact Us Today</a>

<div class="support-band" role="img" aria-label="Glowing circuit board and monitor with technology streams"></div>
<div class="support">
  <h2>Support</h2>
  <h3>We are here to help</h3>
  <p>Our technical support team is always available to you<br>via phone, live chat and support ticketing system.</p>
</div>
<a class="btn" style="left:608px;top:1798px;width:191px;height:30px;font-weight:500">Remote Support Access</a>

<div class="team-photo" role="img" aria-label="Business team meeting around a table"></div>
<div class="logo-tile"><div class="brand"><span class="dot" style="width:20px;height:20px"></span>Zentrik UC</div></div>
<div class="why">
  <h2><span class="dot"></span>Why Zentrik UC</h2>
  <p>Lorem ipsum dolor sit amet, consectetuer adipiscing elit, sed donummy nibh euismod tincidunt ut laoreet dolore magna aliquam erat volutpat. Ut wisi enim ad minim veniam, quis nostrud exerci.</p>
  <ul>
    <li><svg width="16" height="16" viewBox="0 0 16 16"><circle cx="8" cy="8" r="6.5" fill="none" stroke="#0b5ea8" stroke-width="1.3"/><path d="M5 8l2.2 2.2L12 4" fill="none" stroke="#0b5ea8" stroke-width="1.6"/></svg>Duis autem vel eum iriure dolor in hendrerit in vulputate.</li>
    <li><svg width="16" height="16" viewBox="0 0 16 16"><circle cx="8" cy="8" r="6.5" fill="none" stroke="#0b5ea8" stroke-width="1.3"/><path d="M5 8l2.2 2.2L12 4" fill="none" stroke="#0b5ea8" stroke-width="1.6"/></svg>Velit esse olestie consequat, vel illum dolore eu feugiat.</li>
    <li><svg width="16" height="16" viewBox="0 0 16 16"><circle cx="8" cy="8" r="6.5" fill="none" stroke="#0b5ea8" stroke-width="1.3"/><path d="M5 8l2.2 2.2L12 4" fill="none" stroke="#0b5ea8" stroke-width="1.6"/></svg>Nulla facilisis at vero erocumsan et iusto odio dignissim qui.</li>
  </ul>
</div>
<a class="btn" style="left:591px;top:2245px;width:156px;height:40px;border-radius:20px;font-size:15px;font-weight:500">Contact Us Today</a>

<div class="footer-bg" role="img" aria-label="Aerial view of a city skyline in blue tones"></div>

<form class="inquiry">
  <h2>Quick Inquiry</h2>
  <div class="field" style="left:56px;top:87px;width:290px"><span class="ico"><svg width="12" height="12" viewBox="0 0 12 12"><circle cx="6" cy="3.5" r="2.8" fill="#0b5ea8"/><path d="M1 12a5 5 0 0110 0z" fill="#0b5ea8"/></svg></span><span class="ph">First Name*</span></div>
  <div class="field" style="left:361px;top:87px;width:290px"><span class="ico"><svg width="12" height="12" viewBox="0 0 12 12"><circle cx="6" cy="3.5" r="2.8" fill="#0b5ea8"/><path d="M1 12a5 5 0 0110 0z" fill="#0b5ea8"/></svg></span><span class="ph">Last Name*</span></div>
  <div class="field" style="left:56px;top:141px;width:290px"><span class="ico"><svg width="12" height="12" viewBox="0 0 24 24"><path d="M6.6 10.8a15 15 0 006.6 6.6l2.2-2.2 5 1.3V21A18 18 0 013 4h4.5l1.3 5z" fill="#0b5ea8"/></svg></span><span class="ph">Your Phone*</span></div>
  <div class="field" style="left:361px;top:141px;width:290px"><span class="ico"><svg width="12" height="10" viewBox="0 0 12 10"><rect width="12" height="10" fill="#0b5ea8"/><path d="M0 0l6 5 6-5" stroke="#fff" fill="none"/></svg></span><span class="ph">Your Email*</span></div>
  <div class="field" style="left:56px;top:196px;width:595px;height:85px"><span class="ico"><svg width="13" height="11" viewBox="0 0 13 11"><ellipse cx="5" cy="4" rx="5" ry="3.5" fill="#0b5ea8"/><ellipse cx="9" cy="7" rx="4" ry="3" fill="#0b5ea8"/></svg></span><span class="ph">Your Message*</span></div>
  <div class="submit">Submit</div>
</form>

<div class="footer">
  <h4 style="left:143px;top:2810px">Quick Links</h4>
  <ul class="links"><li>Home</li><li>Voice</li><li>Data</li><li>Hardware</li><li>Services Request</li><li>Contact Us</li></ul>
  <h4 style="left:310px;top:2810px">Contact Details</h4>
  <div class="ccol" style="left:310px;top:2850px">
    <div>Accounts</div>
    <div class="row"><svg width="16" height="16" viewBox="0 0 24 24"><path d="M6.6 10.8a15 15 0 006.6 6.6l2.2-2.2 5 1.3V21A18 18 0 013 4h4.5l1.3 5z" fill="none" stroke="#fff" stroke-width="2"/></svg>+612 5550 1191</div>
    <div class="row"><svg width="16" height="12" viewBox="0 0 16 12"><rect x="1" y="1" width="14" height="10" fill="none" stroke="#fff"/><path d="M1 1l7 6 7-6" fill="none" stroke="#fff"/></svg>accounts@harborzentrik.com.au</div>
    <div class="row" style="margin-top:18px"><svg width="12" height="16" viewBox="0 0 12 16"><path d="M6 16S0 9 0 6a6 6 0 0112 0c0 3-6 10-6 10z" fill="#fff"/><circle cx="6" cy="6" r="2" fill="#1b5aa3"/></svg>PO Box 1234, Marlow ACT 2900</div>
    <div style="margin-top:4px">ABN: 12 345 678 901</div>
  </div>
  <div class="ccol" style="left:576px;top:2850px">
    <div>Admin.</div>
    <div class="row"><svg width="16" height="16" viewBox="0 0 24 24"><path d="M6.6 10.8a15 15 0 006.6 6.6l2.2-2.2 5 1.3V21A18 18 0 013 4h4.5l1.3 5z" fill="none" stroke="#fff" stroke-width="2"/></svg>+612 5550 1191</div>
    <div class="row"><svg width="16" height="12" viewBox="0 0 16 12"><rect x="1" y="1" width="14" height="10" fill="none" stroke="#fff"/><path d="M1 1l7 6 7-6" fill="none" stroke="#fff"/></svg>admin@harborzentrik.com.au</div>
    <div style="margin-top:14px;padding-left:8px">Follow Us On</div>
    <div class="social" style="padding-left:8px"><span></span><span></span><span></span></div>
  </div>
  <div class="ccol" style="left:820px;top:2850px">
    <div>Support</div>
    <div class="row"><svg width="16" height="16" viewBox="0 0 24 24"><path d="M6.6 10.8a15 15 0 006.6 6.6l2.2-2.2 5 1.3V21A18 18 0 013 4h4.5l1.3 5z" fill="none" stroke="#fff" stroke-width="2"/></svg>+612 5550 1151</div>
    <div class="row"><svg width="16" height="12" viewBox="0 0 16 12"><rect x="1" y="1" width="14" height="10" fill="none" stroke="#fff"/><path d="M1 1l7 6 7-6" fill="none" stroke="#fff"/></svg>support@harborzentrik.com.au</div>
  </div>
  <div class="brand" style="left:829px;top:2960px;font-size:30px;color:#fff"><span class="dot" style="background:#fff"></span>Zentrik UC</div>
  <div class="copyright">Copyright © 2019 Zentrik UC. All Rights Reserved.&nbsp; Terms &amp; Conditions</div>
</div>

</body>
</html>
```